Business Card Design Project for Architecture and Interior Design company

We need a business card design and logo for an architecture and design firm located in Santiago de Chile. It´s a small company, and the name is "Ostrevo" ("Ostr" from my surname Ostrini, and "arq" for arquitectura or architecture. But it would also be nice that the logo comunicates de Word game "Bella" as beautiful in italian, and "arq" as architecture".
The idea is to give a delicate, elegant and sofisticated, yet fresh image. Would prefer grey black and white colors, but wouldn´t mind to use another additional color.
I allready have a web page www.ostrevo-studio.example, but would like to improve the logo design.
Please contact if any further information is requiered.
Reason: Need a more arquitectural and desing spirit in the cards. Few of them give that idea.

```html
<!DOCTYPE html>
<html lang="es">
<head>
<meta charset="utf-8">
<title>Ostrevo – Tarjeta de presentación</title>
<link rel="stylesheet" href="https://fonts.googleapis.com/css2?family=Arimo:wght@700&display=swap">
<style>
  :root {
    --page: #ffffff;
    --card-grey: #807f7d;
    --band-dark: #3a3836;
    --ink-light: #ffffff;
  }
  * { margin: 0; padding: 0; box-sizing: border-box; }
  html, body {
    width: 1200px;
    height: 706px;
    overflow: hidden;
    background: var(--page);
  }
  .canvas {
    position: relative;
    width: 1200px;
    height: 706px;
    font-family: "Arimo", Arial, sans-serif;
    font-weight: 700;
    color: var(--ink-light);
  }
  .card-face {
    position: absolute;
    left: 36px;
    top: 39px;
    width: 1128px;
    height: 587px;
    background: var(--card-grey);
  }
  .base-band {
    position: absolute;
    left: 36px;
    top: 635px;
    width: 1128px;
    height: 29px;
    background: var(--band-dark);
  }
  .person-name {
    position: absolute;
    left: 100px;
    top: 386px;
    font-size: 54px;
    line-height: 1;
    letter-spacing: 0.5px;
  }
  .contact-list {
    position: absolute;
    left: 101px;
    top: 484px;
    list-style: none;
    font-size: 27px;
    line-height: 37px;
  }
  .brand-name {
    position: absolute;
    right: 94px;
    top: 502px;
    font-size: 86px;
    line-height: 1;
    letter-spacing: 1px;
  }
</style>
</head>
<body>
  <main class="canvas">
    <section class="card-face">
    </section>
    <div class="base-band"></div>

    <h1 class="person-name">Mara Ostrini</h1>
    <ul class="contact-list">
      <li>Contacto: info@ostrevo.example</li>
      <li>Fono: +56 9 55501234</li>
      <li>www.ostrevo-studio.example</li>
    </ul>

    <p class="brand-name">Ostrevo</p>
  </main>
</body>
</html>
```